Legal Journal cover - modern and sylish

We require a cover design for a new, modern and digital legal academic journal. Attached is our logo so you can get an idea of the feel. This academic journal will have several editions per year.Requirements for the cover design:-The feel of the cover is to be modern -In harmony with our logo-While staying uniform and set in its design,

Colors
ec1f27

Requirements
Must have
• 1) Colour. Each edition will use different colours. (So we will need the source files to be able to continue to do this)
• 2) An image section. We would like to be able to put in different image or photo with each edition. So we need to have a section, most likely in the shape of a strip, that can include a different image or photo each edition. This part is where we can put a different image in for each edition. So this section would need to be able to accommodate different types of images. It could be a single square. Or it could be a line (a strip) that an image or images.
• 3) A title for the edition and volume and number. Like this:
• Volume 34, No 2 (2016): Contemporary Issues in Criminal Law
• I have attached a range of journals I found online to serve as inspiration.

```html
<!DOCTYPE html>
<html lang="en">
<head>
<meta charset="utf-8">
<title>Contemporary Issues in Criminal Law – Journal Cover</title>
<link rel="stylesheet" href="https://fonts.googleapis.com/css2?family=Montserrat:wght@500;600&family=Roboto+Condensed:ital,wght@1,700&family=Roboto:wght@400&display=swap">
<style>
  :root {
    --page: #ffffff;
    --paper-top: #e6e6e6;
    --paper-bottom: #f9f9f9;
    --red: #ec1f27;
    --red-deep: #b4161c;
    --ink: #111111;
    --title-grey: #707070;
    --white: #ffffff;
  }
  * { margin: 0; padding: 0; box-sizing: border-box; }
  html, body {
    width: 1200px; height: 1200px; overflow: hidden;
    background: var(--page);
  }
  .cover {
    position: absolute;
    left: 204px; top: 40px;
    width: 792px; height: 1120px;
    background: linear-gradient(170deg, var(--paper-top) 0%, var(--paper-bottom) 100%);
    overflow: hidden;
  }
  .cover-artwork {
    position: absolute;
    left: 0; top: 0;
    width: 100%; height: 500px;
    background: linear-gradient(120deg, var(--red-deep) 0%, var(--red) 65%, var(--red) 100%);
  }
  .issue-meta {
    position: absolute;
    left: 69px; top: 212px;
    font-family: "Montserrat", sans-serif;
    font-weight: 600;
    font-size: 26px;
    line-height: 1.2;
    color: var(--white);
  }
  .emblem {
    position: absolute;
    left: 420px; top: 186px;
    width: 279px; height: 268px;
    background: radial-gradient(ellipse at 50% 45%, #2b2b2b 0%, #111111 70%);
    border-radius: 6px;
  }
  .edition-title {
    position: absolute;
    right: 83px; top: 590px;
    text-align: right;
    font-family: "Roboto Condensed", sans-serif;
    font-style: italic;
    font-weight: 700;
    font-size: 51px;
    line-height: 56px;
    color: var(--title-grey);
    letter-spacing: 0.5px;
  }
  .photo-slot {
    position: absolute;
    border: 4px solid var(--red);
    display: flex; align-items: center; justify-content: center;
    font-family: "Roboto", sans-serif;
    font-weight: 400;
    font-size: 30px;
    color: var(--ink);
  }
  .photo-slot--large { left: 151px; top: 748px; width: 258px; height: 258px; }
  .photo-slot--small { left: 441px; top: 781px; width: 161px; height: 161px; padding-bottom: 20px; }
  .publisher {
    position: absolute;
    left: 584px; top: 1030px;
    display: flex; align-items: center; gap: 10px;
  }
  .publisher-dot {
    width: 40px; height: 40px; border-radius: 50%;
    background: var(--red);
  }
  .publisher-name {
    font-family: "Montserrat", sans-serif;
    font-weight: 600;
    font-size: 22px;
    color: var(--red);
    letter-spacing: 0.5px;
  }
</style>
</head>
<body>
  <main class="cover">
    <div class="cover-artwork" role="img" aria-label="Decorative artwork: layered flowing red waves across the top of the cover"></div>

    <p class="issue-meta">Volume 34<br>No. 2, (2016)</p>

    <div class="emblem" role="img" aria-label="Emblem: scales of justice silhouette"></div>

    <h1 class="edition-title">CONTEMPORARY<br>ISSUES IN CRIMINAL LAW</h1>

    <div class="photo-slot photo-slot--large">photo</div>
    <div class="photo-slot photo-slot--small">photo</div>

    <div class="publisher">
      <span class="publisher-dot"></span>
      <span class="publisher-name">JURIS LENS</span>
    </div>
  </main>
</body>
</html>
```